Business card for medical clinic

I need an upmarket, modern medical/health business card for my clinic

Contact Information for Business Card

name, address, email, qr code

```html
<!DOCTYPE html>
<html lang="en">
<head>
<meta charset="utf-8">
<title>Meridian Care Partners – Business Card</title>
<link rel="stylesheet" href="https://fonts.googleapis.com/css2?family=Montserrat:wght@400;600;700&display=swap">
<style>
  :root {
    --stage: #2a323d;
    --white: #ffffff;
    --navy: #1d3b5e;
    --deep: #1f4d74;
    --sky: #239bd3;
    --brand: #1b5d8f;
  }
  * { margin: 0; padding: 0; box-sizing: border-box; }
  html, body { width: 1200px; height: 900px; overflow: hidden; }
  body {
    background: var(--stage);
    font-family: "Montserrat", sans-serif;
    position: relative;
  }
  .card {
    position: absolute;
    left: 286px;
    width: 604px;
    height: 362px;
    border-radius: 16px;
    overflow: hidden;
  }
  .card-front { top: 57px; background: var(--white); }
  .card-back {
    top: 470px;
    background: linear-gradient(135deg, var(--navy) 0%, #235f8c 45%, var(--sky) 100%);
  }

  .brand {
    position: absolute;
    display: flex;
    align-items: center;
    gap: 14px;
    font-weight: 600;
    letter-spacing: 0.06em;
    text-transform: uppercase;
    white-space: nowrap;
  }
  .brand-dot { border-radius: 50%; flex: none; }
  .card-front .brand {
    left: 0; right: 0; top: 58px;
    justify-content: center;
    color: var(--brand);
    font-size: 28px;
  }
  .card-front .brand-dot { width: 36px; height: 36px; border: 3px solid var(--brand); }
  .card-back .brand {
    left: 0; right: 0; top: 160px;
    justify-content: center;
    color: var(--white);
    font-size: 32px;
  }
  .card-back .brand-dot { width: 42px; height: 42px; border: 3px solid var(--white); }

  .name-band {
    position: absolute;
    top: 214px; left: 0; right: 0; height: 42px;
    background: linear-gradient(90deg, var(--sky) 0%, var(--deep) 100%);
    display: flex; align-items: center; justify-content: center;
    color: var(--white);
  }
  .person-name { font-weight: 700; font-size: 23px; }
  .person-role {
    font-size: 14px; margin-left: 8px; padding-left: 8px;
    border-left: 1px solid rgba(255,255,255,0.8);
    line-height: 18px;
  }
  .contact-band {
    position: absolute;
    top: 262px; left: 0; right: 0; height: 88px;
    background: linear-gradient(90deg, var(--deep) 0%, var(--sky) 100%);
    color: var(--white);
    font-size: 14px;
  }
  .contact-item { position: absolute; display: flex; align-items: center; gap: 10px; line-height: 16px; }
  .contact-item svg { width: 12px; height: 12px; fill: var(--white); flex: none; }
  .contact-phone { left: 27px; top: 22px; }
  .contact-email { left: 27px; top: 50px; }
  .contact-web { right: 22px; top: 16px; text-align: right; }
  .contact-address { right: 22px; top: 44px; text-align: right; }
  .contact-address svg { width: 12px; height: 15px; align-self: flex-start; margin-top: 1px; }
</style>
</head>
<body>
  <section class="card card-front" aria-label="Business card front">
    <div class="brand"><span class="brand-dot"></span>Meridian Care Partners</div>
    <div class="name-band">
      <span class="person-name">Marlo Fenwick</span>
      <span class="person-role">CEO &amp; Founder</span>
    </div>
    <div class="contact-band">
      <div class="contact-item contact-phone">
        <svg viewBox="0 0 24 24" aria-hidden="true"><path d="M6.6 10.8a15.1 15.1 0 0 0 6.6 6.6l2.2-2.2c.3-.3.7-.4 1-.2 1.1.4 2.3.6 3.6.6.6 0 1 .4 1 1V20c0 .6-.4 1-1 1A17 17 0 0 1 3 4c0-.6.4-1 1-1h3.5c.6 0 1 .4 1 1 0 1.3.2 2.5.6 3.6.1.3 0 .7-.2 1z"/></svg>
        <span>215-555-0142</span>
      </div>
      <div class="contact-item contact-email">
        <svg viewBox="0 0 24 24" aria-hidden="true"><path d="M2 5h20v14H2z M3 6l9 7 9-7" /></svg>
        <span>info@meridiancarepartners.com</span>
      </div>
      <div class="contact-item contact-web">
        <span>www.meridiancarepartners.com</span>
        <svg viewBox="0 0 24 24" aria-hidden="true"><circle cx="12" cy="12" r="11"/></svg>
      </div>
      <div class="contact-item contact-address">
        <span>48 Harbor Ridge Road, Suite 210<br>Linwood, PA 19061</span>
        <svg viewBox="0 0 24 30" aria-hidden="true"><path d="M12 0a11 11 0 0 0-11 11c0 8 11 19 11 19s11-11 11-19A11 11 0 0 0 12 0zm0 15a4 4 0 1 1 0-8 4 4 0 0 1 0 8z"/></svg>
      </div>
    </div>
  </section>

  <section class="card card-back" aria-label="Business card back">
    <div class="brand"><span class="brand-dot"></span>Meridian Care Partners</div>
  </section>
</body>
</html>
```